Free Range Egg Farmer wants a Egg Carton Design

We need a design for Free Range Egg carton. Our company name is "BrookHaven The Craft of Growing"

We run a environmentally friendly farm in Gippsland VIC and we produce Free Range Eggs and Pasture Fed Meats in open pasture.

We also run a farm stay business in a very high energy star rating house.
The farm guest participates in our farm activity such as looking after farm animals, maintaining the vegetable garden, cooking fresh food, Yoga and Meditation.

We would like to see designs with our logo and something alternative rather than a typical free range egg cartons.

The team had a meeting and came up with one idea.
"The meditating hen" with thought bubble which we can change the hen's thought by printing batch.
You could either use this idea or create your own.

I have attached 3 photos close to my image as examples.
I also have attached the typical free range egg cartons as examples.

Sticker size is attached. The sticker fits between the case closure system. So there is no need to make spaces for the closure gaps.
Please place Best Before stamp area at the top right corner of the main (middle) section.
Updates

I have post an update to my brief. Please have a look again. BrookHaven

Industry/Entity Type

Printing

Requirements
Must have
• Company name,
Address,
contact number,
social page link,
best before date (space to put the stamp on)
12 Free Range Eggs xxx g
Nutrition info

```html
<!DOCTYPE html>
<html lang="en">
<head>
<meta charset="utf-8">
<title>BrookHaven Free Range Egg Carton Sticker</title>
<link rel="stylesheet" href="https://fonts.googleapis.com/css2?family=Sansita:wght@800&family=Roboto+Condensed:wght@400;700&family=Roboto:wght@300&display=swap">
<style>
  :root {
    --canvas: #3a3b3b;
    --yellow-light: #fff23a;
    --yellow-deep: #ffcc0a;
    --red-orange: #e8483a;
    --orange: #f4a03c;
    --brand-red: #e8202a;
    --ring-orange: #e0652a;
    --white: #ffffff;
    --logo-dark: #3c3c3c;
    --bubble: #fbd0a6;
    --ink: #222222;
  }
  * { margin: 0; padding: 0; box-sizing: border-box; }
  html, body { width: 1200px; height: 1000px; overflow: hidden; }
  body {
    background: var(--canvas);
    position: relative;
    font-family: "Roboto Condensed", Arial, sans-serif;
  }
  .panel { position: absolute; left: 76px; width: 1038px; }
  .panel-top {
    top: 36px; height: 194px;
    background: linear-gradient(90deg, var(--yellow-deep), var(--yellow-light));
  }
  .panel-main {
    top: 247px; height: 485px; overflow: hidden;
    background: linear-gradient(90deg, var(--red-orange) 0%, var(--orange) 50%, var(--yellow-deep) 100%);
  }
  .panel-bottom {
    top: 750px; height: 194px;
    background: linear-gradient(90deg, var(--yellow-light), var(--yellow-deep));
  }
  .flipped { position: absolute; inset: 0; transform: rotate(180deg); }

  .brand-seal {
    position: absolute; border-radius: 50%;
    background: var(--logo-dark);
    border: 3px solid var(--white);
    display: flex; align-items: center; justify-content: center;
    color: var(--white);
    font-family: "Roboto Condensed", Arial, sans-serif;
    font-weight: 700; font-size: 17px;
  }

  .headline {
    position: absolute;
    font-family: "Sansita", Georgia, serif;
    font-weight: 800; color: var(--brand-red);
    white-space: nowrap; line-height: 1;
  }
  .flap-headline { font-size: 64px; }

  /* top flap (printed upside down) */
  .nutrition-box {
    position: absolute; left: 774px; top: 48px; width: 216px; height: 96px;
    background: var(--white); border: 2px solid var(--brand-red); border-radius: 16px;
  }
  .nutrition-label {
    position: absolute; left: 8px; top: 6px;
    font-family: "Roboto", Arial, sans-serif; font-weight: 300; font-size: 11px; color: var(--ink);
  }
  .panel-top .headline { left: 269px; top: 58px; }
  .panel-top .brand-seal { left: 59px; top: 48px; width: 106px; height: 106px; }

  /* main face */
  .brand-card {
    position: absolute; left: 38px; top: 34px; width: 150px; height: 180px;
    border: 2px solid var(--white); border-radius: 16px; text-align: center;
  }
  .brand-card .brand-seal { left: 22px; top: 14px; width: 102px; height: 102px; }
  .brand-card-text {
    position: absolute; left: 0; right: 0; top: 122px;
    color: var(--white); font-weight: 700; font-size: 15px; line-height: 20px;
  }
  .hen-art {
    position: absolute; left: 206px; top: 184px; width: 190px; height: 230px;
    border-radius: 48% 48% 42% 42%;
    background: radial-gradient(ellipse at 50% 45%, #ffffff 0%, #f3f1ec 70%, #e9e6de 100%);
  }
  .thought-bubble {
    position: absolute; border-radius: 50%;
    background: var(--bubble); border: 2px solid var(--ring-orange);
  }
  .bubble-s { left: 362px; top: 140px; width: 32px; height: 32px; }
  .bubble-m { left: 386px; top: 80px; width: 52px; height: 52px; }
  .bubble-l { left: 446px; top: 54px; width: 62px; height: 62px; }
  .title-disc {
    position: absolute; left: 476px; top: 61px; width: 272px; height: 272px;
    border-radius: 50%; background: var(--white);
    box-shadow: 0 4px 10px rgba(120,40,0,0.25);
  }
  .title-disc::after {
    content: ""; position: absolute; inset: 14px;
    border: 2px solid var(--ring-orange); border-radius: 50%;
  }
  .title-disc .headline {
    position: relative; display: block; text-align: center; white-space: normal;
    font-size: 58px; line-height: 68px; margin-top: 34px;
  }
  .count-badge {
    position: absolute; left: 858px; top: 143px; width: 142px; height: 142px;
    border-radius: 50%; background: var(--yellow-deep);
    border: 3px solid var(--brand-red);
    display: flex; align-items: center; justify-content: center;
  }
  .count-badge-inner {
    width: 118px; height: 118px; border-radius: 50%;
    background: var(--white); border: 10px solid var(--brand-red);
    color: var(--brand-red); text-align: center; font-weight: 700;
    display: flex; flex-direction: column; justify-content: center;
  }
  .count-number { font-size: 24px; line-height: 24px; }
  .count-label { font-size: 14px; line-height: 16px; }
  .best-before {
    position: absolute; left: 796px; top: 302px; width: 204px; height: 93px;
    background: var(--white); border: 4px solid var(--brand-red);
    padding: 6px 8px; font-weight: 700; font-size: 12px; color: var(--ink);
  }
  .egg-field {
    position: absolute; left: 0; bottom: 0; width: 100%; height: 62px;
    background: linear-gradient(180deg, #fbfaf6, #efede6);
    border-top-left-radius: 30px 20px; border-top-right-radius: 30px 20px;
  }

  /* bottom flap */
  .panel-bottom .brand-seal { left: 60px; top: 49px; width: 106px; height: 106px; }
  .panel-bottom .headline { left: 286px; top: 62px; }
  .contact-box {
    position: absolute; left: 776px; top: 33px; width: 262px; height: 131px;
    background: var(--white); padding: 28px 40px;
    font-family: "Roboto", Arial, sans-serif; font-weight: 300; font-size: 18px; line-height: 27px; color: var(--ink);
  }
</style>
</head>
<body>

<section class="panel panel-top">
  <div class="flipped">
    <div class="nutrition-box">
      <span class="nutrition-label">Nutrition info</span>
    </div>
    <h2 class="headline flap-headline">Free Range Egg</h2>
    <div class="brand-seal">BrookHaven</div>
  </div>
</section>

<section class="panel panel-main">
  <div class="brand-card">
    <div class="brand-seal">BrookHaven</div>
    <p class="brand-card-text">BrookHaven<br>The Craft of Growing</p>
  </div>

  <div class="thought-bubble bubble-s"></div>
  <div class="thought-bubble bubble-m"></div>
  <div class="thought-bubble bubble-l"></div>
  <div class="hen-art" role="img" aria-label="Illustration of a white hen standing and thinking"></div>

  <div class="title-disc">
    <h1 class="headline">Free<br>Range<br>Egg</h1>
  </div>

  <div class="count-badge">
    <div class="count-badge-inner">
      <span class="count-number">12</span>
      <span class="count-label">Free Range</span>
      <span class="count-label">Eggs</span>
      <span class="count-label">xxx g</span>
    </div>
  </div>

  <div class="best-before">BEST BEFORE</div>

  <div class="egg-field" role="img" aria-label="Illustration of a field of white eggs along the bottom edge"></div>
</section>

<section class="panel panel-bottom">
  <div class="brand-seal">BrookHaven</div>
  <h2 class="headline flap-headline">Free Range Egg</h2>
  <div class="contact-box">
    Address,<br>contact number,<br>social page link,
  </div>
</section>

</body>
</html>
```